Business Card Design Project

I have just chosen a logo and would now like this designed onto a business card for my hair salon. I would like it to be classy not to busy and have a wow factor when people look at them
Has to Include on card:
Logo Design
And business details below
Kellie-ann Drummond (owner)
0482 736 219
Rdw@vomblet.com.au
71 Willowmere Rise Corvin Cove
Logo is now attached please provide designs
Hair

```html
<!DOCTYPE html>
<html lang="en">
<head>
<meta charset="utf-8">
<title>Maren Hair House – Business Card</title>
<link href="https://fonts.googleapis.com/css2?family=Cinzel:wght@400;600&display=swap" rel="stylesheet">
<style>
  :root {
    --backdrop: #e9e4dc;
    --card-white: #ffffff;
    --teal: #3aafbd;
    --teal-deep: #2f9aa8;
    --magenta: #d4126f;
    --ink: #4a4a4a;
    --shadow: rgba(60, 45, 30, 0.28);
  }
  * { box-sizing: border-box; margin: 0; padding: 0; }
  html, body {
    width: 1184px;
    height: 1200px;
    overflow: hidden;
    background: var(--backdrop);
    font-family: "Cinzel", "Times New Roman", serif;
  }
  .sheet {
    position: relative;
    width: 1184px;
    height: 1200px;
  }
  .card {
    position: absolute;
    left: 142px;
    width: 900px;
    height: 550px;
    background: var(--card-white);
    box-shadow: 0 10px 28px var(--shadow), 0 2px 4px var(--shadow);
  }
  .card--front { top: 40px; }
  .card--back { top: 610px; }

  .front-panel {
    position: absolute;
    inset: 0;
    width: 900px;
    height: 550px;
  }
  .front-name {
    position: absolute;
    inset: 0;
    display: flex;
    flex-direction: column;
    align-items: center;
    justify-content: center;
    color: var(--card-white);
    font-weight: 400;
    line-height: 1;
    letter-spacing: 0.02em;
  }
  .front-name__top { font-size: 104px; }
  .front-name__bottom { font-size: 66px; margin-top: 14px; }

  .back-content {
    position: absolute;
    top: 70px;
    right: 90px;
    width: 540px;
    text-align: center;
  }
  .back-name {
    color: var(--magenta);
    font-weight: 400;
    line-height: 1;
  }
  .back-name__top { display: block; font-size: 78px; }
  .back-name__bottom { display: block; font-size: 48px; margin-top: 10px; }
  .owner-name {
    margin-top: 44px;
    color: var(--magenta);
    font-size: 30px;
    font-weight: 600;
  }
  .owner-role {
    margin-top: 4px;
    color: var(--teal);
    font-size: 24px;
  }
  .contact {
    margin-top: 22px;
    list-style: none;
    color: var(--ink);
    font-size: 22px;
    line-height: 1.45;
  }
</style>
</head>
<body>
<main class="sheet">
  <section class="card card--front" aria-label="Card front">
    <svg class="front-panel" viewBox="0 0 900 550" aria-hidden="true">
      <defs>
        <linearGradient id="teal-fill" x1="0" y1="0" x2="1" y2="1">
          <stop offset="0" stop-color="var(--teal)"/>
          <stop offset="1" stop-color="var(--teal-deep)"/>
        </linearGradient>
      </defs>
      <path fill="url(#teal-fill)"
        d="M50,20 H850 A30 30 0 0 0 880,50 V500 A30 30 0 0 0 850,530 H50 A30 30 0 0 0 20,500 V50 A30 30 0 0 0 50,20 Z"/>
    </svg>
    <h1 class="front-name">
      <span class="front-name__top">Maren</span>
      <span class="front-name__bottom">Hair House</span>
    </h1>
  </section>

  <section class="card card--back" aria-label="Card back">
    <div class="back-content">
      <h2 class="back-name">
        <span class="back-name__top">Maren</span>
        <span class="back-name__bottom">Hair House</span>
      </h2>
      <p class="owner-name">Kellie-ann Drummond</p>
      <p class="owner-role">Owner</p>
      <ul class="contact">
        <li>0482 736 219</li>
        <li>Rdw@vomblet.com.au</li>
        <li>71 Willowmere Rise Corvin Cove</li>
      </ul>
    </div>
  </section>
</main>
</body>
</html>
```